Continuing Professional Development Seminars
Power Point Template
• 11 juin 2011 15:52 rubenqol
thanks Velmoro
• 9 juin 2011 11:07 Velmoro
congrats your first project :)
• 9 juin 2011 02:48 tkvolaris
rubenqol - can you please upload a new draft that has the following slides:
1 - The title slide from draft#15 (I think this might be exactly the same in all subsequent drafts)
2 - The content slide from draft#15
3 - The content slide from draft#66
4 - The content slide from draft#68
5 - The last slide from draft#69
6 - The last slide from draft#15
I would like to see both of the end slides in the same draft.
Thanks.
• 7 juin 2011 08:20 tkvolaris
Thank you to all the designers who have submitted designs to date. The quality of the work is outstanding and is making the decision difficult.
I am still considering ALL the designs and will probably make a final decision soon. However, the designs that seem to stand out at the moment include (in no particular order) draft#50/draft#72, draft#15 (and the variations), draft#62 and draft#54.
• 6 juin 2011 06:31 tkvolaris
Draft#15 – can you please make the following changes:
1. Replace the last slide with a variant of the first slide. This new slide should be the same as the first slide, but with the following changes:
• The colours of the main background graphic should be reversed – so that becomes a red graphic with a blue stipe (instead of a blue graphic with a red stripe).
• Change the text - “Welcome to our Presentation” to “Thank you”.
• Change the white text (location and date) to the contact details you currently have on the last slide.
2. Can we try three small variations to the header on the content slides? Firstly, can you make the line under the presentation header about an inch smaller (so that it doesn’t go all the way to the logo). Secondly, can you please do a variant that reverses the logo and the header title (so that the logo is on the right and the presentation title is on the left). Thirdly, can you try a variant that doesn’t have the presentation header at all – only the logo? I would prefer having a look at all three slides to see how it looks. Thanks.
• 2 juin 2011 06:02 tkvolaris
Some of the recent designs have been very good. I particularly like the very bold graphical styles on the front pages whilst I prefer the more minimalist approach to the content slides.
I know that I said previously to try using our logo as a background watermark. However, on second thoughts I don’t think it really works. The watermarks are OK on the first slides, but on the content slides it is very distracting.
So far, my favourite designs are draft#15 and drafts#25-26. However, many of the designs have things I like or don’t like. Specifically,
• Draft#25 and Draft #26 – These designs are very effective. A bold front page and simple content pages. I think we would need to lose the watermarks on the content pages, but otherwise, these designs are on the right track.
• Draft#23 – I like the footer design of each content slide. Very simple and elegant.
• Draft#15 – perhaps my favourite design so far. Good bold first slide. The content slides are also good – maybe a little too busy as the moment?
• Draft#9 and Draft#10 – The first slides in these designs are very good. I like the strong bold designs. The content pages don’t really work – too much graphical background and not enough white space for content. One thing I like about these designs is the reverse colours of the background on the final slides.
Some of the other designs have similar good and bad points. However, I think I would be repeating myself if I discussed each one.
In summary, I like the first slides that are bold and emphasise our brand. The content slides should be simple, elegant and consistent.
• 31 mai 2011 19:56 tkvolaris
When I was looking through other projects on this website, there is one that I found that seems to be very effective. The project name is "Brisk Lanterns PowerPoint Template" and the design is draft#39.
I am not suggesting that I want a copy or a redraft of this design. It is just an example of something that I like.
• 31 mai 2011 19:47 tkvolaris
I like the designs that are creatively using the "swirls" on our logo. The first pages in draft#9 and draft#10 are interesting. I also didn't mind the first page in draft#11 (but note that it has been withdrawn?).
I think the logo needs to be more subtle on the content pages - maybe in the bottom right corner? Also maybe could use the logo as a watermark? Draft#4 uses a watermark, but being in the middle of the page, it might be a little distracting.

```html
<!DOCTYPE html>
<html lang="en">
<head>
<meta charset="utf-8">
<title>KVEN Seminar Slide Template</title>
<link rel="stylesheet" href="https://fonts.googleapis.com/css2?family=Open+Sans:wght@400;600;700&display=swap">
<style>
  :root {
    --stage: #111214;
    --brand-blue: #2b5cab;
    --brand-blue-dark: #1d4690;
    --brand-red: #e0262b;
    --ink: #1e2a3a;
    --muted: #8a8f96;
    --paper: #ffffff;
    --paper-shade: #eef0f3;
    --grid: #d5d8dd;
  }
  * { box-sizing: border-box; margin: 0; padding: 0; }
  html, body { width: 1200px; height: 907px; overflow: hidden; background: var(--stage); }
  body { font-family: "Open Sans", Arial, sans-serif; color: var(--ink); position: relative; }

  .slide { position: absolute; width: 540px; height: 400px; overflow: hidden; background: var(--paper); }
  .slide--title { left: 40px; top: 30px; }
  .slide--content-a { left: 620px; top: 30px; }
  .slide--content-b { left: 40px; top: 477px; }
  .slide--closing { left: 620px; top: 477px; }
  .slide__bg { position: absolute; inset: 0; width: 100%; height: 100%; }

  .brand { position: absolute; display: flex; align-items: center; gap: 6px;
    font-weight: 700; color: var(--brand-blue); letter-spacing: 1px; }
  .brand__dot { width: 12px; height: 12px; border-radius: 50%; background: var(--brand-red); }
  .brand--large { font-size: 44px; }
  .brand--large .brand__dot { width: 16px; height: 16px; }
  .brand--small { font-size: 22px; }
  .brand--small .brand__dot { width: 9px; height: 9px; }

  .title-block { position: absolute; left: 0; right: 0; text-align: center; }
  .title-block__title { font-size: 25px; font-weight: 400; color: var(--brand-blue); }
  .title-block__desc { font-size: 16px; color: var(--brand-red); margin-top: 4px; }
  .site-url { position: absolute; left: 0; right: 0; top: 350px; text-align: center;
    color: var(--paper); font-size: 12px; font-weight: 600; }

  .heading { position: absolute; }
  .heading__title { font-size: 20px; font-weight: 700; color: var(--brand-blue); letter-spacing: .3px; }
  .heading__title em { font-style: normal; color: var(--brand-red); }
  .heading__sub { font-size: 11px; color: var(--ink); margin-top: 1px; }

  .group-list { position: absolute; list-style: none; }
  .group-list li { position: relative; padding-left: 14px; margin-bottom: 9px; }
  .group-list li::before { content: ""; position: absolute; left: 0; top: 4px;
    width: 6px; height: 6px; border-radius: 50%; border: 1.5px solid var(--ink); }
  .group-list h3 { font-size: 11px; font-weight: 700; color: var(--ink); }
  .group-list p { font-size: 7.5px; line-height: 1.35; color: var(--muted); width: 140px; }

  .chart { position: absolute; }

  .closing-text { position: absolute; left: 0; right: 0; top: 212px; text-align: center; }
  .closing-text__title { font-size: 24px; font-weight: 700; color: var(--ink); }
  .closing-text__author { font-size: 17px; font-weight: 700; color: var(--ink); margin-top: 2px; }
</style>
</head>
<body>

<!-- Title slide -->
<section class="slide slide--title" aria-label="Title slide">
  <svg class="slide__bg" viewBox="0 0 540 400" preserveAspectRatio="none" aria-hidden="true">
    <defs>
      <linearGradient id="whiteFace" x1="0" y1="0" x2="0" y2="1">
        <stop offset="0" stop-color="#ffffff"/><stop offset="1" stop-color="#e9ecf1"/>
      </linearGradient>
    </defs>
    <rect width="540" height="400" fill="var(--brand-blue)"/>
    <path d="M0 42 Q270 -8 540 42 L540 318 Q270 372 0 318 Z" fill="url(#whiteFace)"/>
    <path d="M30 52 Q270 8 510 52" fill="none" stroke="var(--brand-red)" stroke-width="3"/>
    <path d="M60 275 Q270 240 480 275" fill="none" stroke="#f2c9cb" stroke-width="6"/>
    <path d="M80 285 Q270 255 460 285" fill="none" stroke="#cad7ee" stroke-width="5"/>
    <path d="M0 330 Q270 288 540 330" fill="none" stroke="var(--brand-red)" stroke-width="3"/>
    <path d="M0 322 Q270 280 540 322" fill="none" stroke="#ffffff" stroke-width="2"/>
  </svg>
  <div class="brand brand--large" style="left:180px; top:118px;"><span class="brand__dot"></span>KVEN</div>
  <div class="title-block" style="top:200px;">
    <h1 class="title-block__title">TITLE OF PRESENTATION</h1>
    <p class="title-block__desc">Description</p>
  </div>
  <p class="site-url">www.kven.com.au</p>
</section>

<!-- Content slide A -->
<section class="slide slide--content-a" aria-label="Content slide with logo right">
  <svg class="slide__bg" viewBox="0 0 540 400" preserveAspectRatio="none" aria-hidden="true">
    <defs>
      <linearGradient id="pageShadeA" x1="0" y1="0" x2="0" y2="1">
        <stop offset="0" stop-color="#ffffff"/><stop offset="1" stop-color="var(--paper-shade)"/>
      </linearGradient>
    </defs>
    <rect width="540" height="400" fill="url(#pageShadeA)"/>
    <path d="M0 340 Q270 300 540 340 L540 400 L0 400 Z" fill="var(--brand-blue)"/>
    <path d="M0 334 Q270 294 540 334" fill="none" stroke="var(--brand-red)" stroke-width="3"/>
  </svg>
  <div class="heading" style="left:28px; top:18px;">
    <h2 class="heading__title">SAMPLES OF CONTENT <em>LIST</em></h2>
    <p class="heading__sub">Description in this line</p>
  </div>
  <div class="brand brand--small" style="left:455px; top:22px;"><span class="brand__dot"></span>KVEN</div>
  <ul class="group-list" style="left:28px; top:80px;">
    <li><h3>Group 3</h3><p>Short note on this point with a few words of detail to support the main idea.</p></li>
    <li><h3>Group 4</h3><p>Short note on this point with a few words of detail to support the main idea.</p></li>
  </ul>
  <ul class="group-list" style="left:290px; top:80px;">
    <li><h3>Group 3</h3><p>Short note on this point with a few words of detail to support the main idea.</p></li>
    <li><h3>Group 4</h3><p>Short note on this point with a few words of detail to support the main idea.</p></li>
    <li><h3>Group 5</h3><p>Short note on this point with a few words of detail to support the main idea.</p></li>
    <li><h3>Group 6</h3><p>Short note on this point with a few words of detail to support the main idea.</p></li>
  </ul>
  <svg class="chart" style="left:28px; top:195px;" width="240" height="100" viewBox="0 0 240 100" aria-label="Bar chart of four groups">
    <g stroke="var(--grid)" stroke-width="1">
      <line x1="10" y1="5" x2="235" y2="5"/><line x1="10" y1="20" x2="235" y2="20"/>
      <line x1="10" y1="35" x2="235" y2="35"/><line x1="10" y1="50" x2="235" y2="50"/>
      <line x1="10" y1="65" x2="235" y2="65"/><line x1="10" y1="80" x2="235" y2="80"/>
    </g>
    <line x1="10" y1="0" x2="10" y2="95" stroke="var(--muted)"/>
    <line x1="10" y1="95" x2="235" y2="95" stroke="var(--muted)"/>
    <rect x="22" y="15" width="26" height="80" fill="var(--brand-blue)"/>
    <rect x="78" y="60" width="26" height="35" fill="var(--brand-red)"/>
    <rect x="134" y="82" width="26" height="13" fill="var(--brand-blue)"/>
    <rect x="190" y="84" width="26" height="11" fill="var(--brand-red)"/>
  </svg>
</section>

<!-- Content slide B -->
<section class="slide slide--content-b" aria-label="Content slide with logo left">
  <svg class="slide__bg" viewBox="0 0 540 400" preserveAspectRatio="none" aria-hidden="true">
    <defs>
      <linearGradient id="pageShadeB" x1="0" y1="0" x2="0" y2="1">
        <stop offset="0" stop-color="#ffffff"/><stop offset="1" stop-color="var(--paper-shade)"/>
      </linearGradient>
    </defs>
    <rect width="540" height="400" fill="url(#pageShadeB)"/>
    <path d="M0 352 Q270 316 540 352 L540 400 L0 400 Z" fill="var(--brand-blue)"/>
    <path d="M0 345 Q270 309 540 345" fill="none" stroke="var(--brand-red)" stroke-width="3"/>
  </svg>
  <div class="brand brand--small" style="left:24px; top:26px;"><span class="brand__dot"></span>KVEN</div>
  <div class="heading" style="right:24px; top:18px; text-align:right;">
    <h2 class="heading__title">SAMPLES OF CONTENT <em>LIST</em></h2>
    <p class="heading__sub">Description in this line</p>
  </div>
  <svg class="chart" style="left:20px; top:88px;" width="250" height="220" viewBox="0 0 250 220" aria-label="Bar chart of four groups">
    <g font-size="8" fill="var(--ink)" text-anchor="end" font-family="Open Sans, sans-serif">
      <text x="12" y="199">0</text><text x="12" y="174">1</text><text x="12" y="149">2</text>
      <text x="12" y="124">3</text><text x="12" y="99">4</text><text x="12" y="74">5</text>
      <text x="12" y="49">6</text><text x="12" y="24">7</text>
    </g>
    <g stroke="var(--grid)" stroke-width="1">
      <line x1="18" y1="21" x2="245" y2="21"/><line x1="18" y1="46" x2="245" y2="46"/>
      <line x1="18" y1="71" x2="245" y2="71"/><line x1="18" y1="96" x2="245" y2="96"/>
      <line x1="18" y1="121" x2="245" y2="121"/><line x1="18" y1="146" x2="245" y2="146"/>
      <line x1="18" y1="171" x2="245" y2="171"/>
    </g>
    <line x1="18" y1="10" x2="18" y2="196" stroke="var(--muted)"/>
    <line x1="18" y1="196" x2="245" y2="196" stroke="var(--muted)"/>
    <rect x="32" y="41" width="28" height="155" fill="var(--brand-blue)"/>
    <rect x="88" y="121" width="28" height="75" fill="var(--brand-red)"/>
    <rect x="144" y="166" width="28" height="30" fill="var(--brand-blue)"/>
    <rect x="200" y="168" width="28" height="28" fill="var(--brand-red)"/>
    <g font-size="7.5" font-weight="700" fill="var(--ink)" text-anchor="middle" font-family="Open Sans, sans-serif">
      <text x="46" y="208">Group 1</text><text x="102" y="208">Group 2</text>
      <text x="158" y="208">Group 3</text><text x="214" y="208">Group 4</text>
    </g>
  </svg>
  <ul class="group-list" style="left:300px; top:92px;">
    <li><h3>Group 3</h3><p>Short note on this point with a few words of detail to support the main idea.</p></li>
    <li><h3>Group 4</h3><p>Short note on this point with a few words of detail to support the main idea.</p></li>
    <li><h3>Group 5</h3><p>Short note on this point with a few words of detail to support the main idea.</p></li>
    <li><h3>Group 6</h3><p>Short note on this point with a few words of detail to support the main idea.</p></li>
  </ul>
</section>

<!-- Closing slide -->
<section class="slide slide--closing" aria-label="Closing slide">
  <svg class="slide__bg" viewBox="0 0 540 400" preserveAspectRatio="none" aria-hidden="true">
    <defs>
      <linearGradient id="pageShadeC" x1="0" y1="0" x2="0" y2="1">
        <stop offset="0" stop-color="#ffffff"/><stop offset="1" stop-color="var(--paper-shade)"/>
      </linearGradient>
    </defs>
    <rect width="540" height="400" fill="url(#pageShadeC)"/>
    <path d="M0 0 H540 V22 Q270 52 0 22 Z" fill="var(--brand-blue)"/>
    <path d="M0 30 Q270 60 540 30" fill="none" stroke="var(--brand-red)" stroke-width="3"/>
    <path d="M0 352 Q270 316 540 352 L540 400 L0 400 Z" fill="var(--brand-blue)"/>
    <path d="M0 345 Q270 309 540 345" fill="none" stroke="var(--brand-red)" stroke-width="3"/>
  </svg>
  <div class="brand brand--large" style="left:186px; top:100px; font-size:38px;"><span class="brand__dot"></span>KVEN</div>
  <div class="closing-text">
    <h2 class="closing-text__title">THANK YOU FOR YOU ATTENTION</h2>
    <p class="closing-text__author">Author</p>
  </div>
</section>

</body>
</html>
```